Halvard Quarry Company needs a company newsletter template

We need a 2-page editable newsletter template, that we can update monthly with various information and pictures. We would like an area to include our values: Be Safe, Be Honest, Be Responsible, Be Respectful, Be Great. Ideally we would have 2-3 bulk text areas to highlight different things each month, with area we an update a picture from time to time and maybe some text areas where we can add a fun fact type thing. Some of the areas we will include are production milestones (if any), monthly tenure, monthly new hires, highlighting an employee that demonstrates our value, community engagement, upcoming holidays/events, press releases. The exact content will likely change month to month but these will be some of the frequent topics. We are a copper Mine in northern Yukon. I've attached our Brand Guidelines and logo files. Our website is brelcoreworks.com if you want to see the style and type of photos from our site

```html
<!DOCTYPE html>
<html lang="en">
<head>
<meta charset="utf-8">
<title>Halvard Matters Newsletter</title>
<link rel="stylesheet" href="https://fonts.googleapis.com/css2?family=Montserrat:wght@500;600;700;800&family=Open+Sans:wght@400;600&display=swap">
<style>
:root{
  --brown:#6a3a22;
  --brown-dark:#4e2917;
  --gold:#f0b234;
  --gold-soft:#f7d27f;
  --ink:#2f2f2f;
  --muted:#6f6f6f;
  --rule:#e2dcd2;
  --canvas:#ececec;
  --paper:#ffffff;
}
*{box-sizing:border-box;margin:0;padding:0}
html,body{width:1200px;height:2832px;overflow:hidden;background:var(--canvas)}
body{font-family:"Open Sans",Arial,sans-serif;color:var(--ink);padding:46px 80px;display:flex;flex-direction:column;gap:46px}
.page{width:1040px;height:1346px;background:var(--paper);box-shadow:0 6px 24px rgba(0,0,0,.12);display:flex;flex-direction:column;overflow:hidden}
h1,h2,h3,h4{font-family:"Montserrat",Arial,sans-serif}
p{font-size:13px;line-height:1.55;color:var(--muted)}

/* page 1 */
.masthead{height:150px;flex:none;display:flex;align-items:center;padding:0 56px;gap:40px}
.brand{display:flex;align-items:center;gap:10px;width:200px}
.brand-square{width:26px;height:26px;background:var(--gold)}
.brand-name{font-family:"Montserrat",sans-serif;font-weight:700;font-size:15px;color:var(--brown);letter-spacing:1px}
.title-block{flex:1;text-align:center;padding-right:200px}
.kicker{font-family:"Montserrat",sans-serif;font-weight:600;font-size:24px;letter-spacing:6px;color:var(--brown)}
.title{font-family:"Montserrat",sans-serif;font-weight:800;font-size:72px;line-height:1;letter-spacing:1px}
.title .news{color:var(--brown)}
.title .letter{color:var(--gold)}

.hero{height:240px;flex:none;display:flex;margin:0 56px}
.hero-panel{width:430px;background:var(--gold);padding:30px 32px}
.hero-panel h2{font-size:22px;font-weight:800;color:var(--brown-dark);margin-bottom:12px}
.hero-panel p{color:#5a3a1a}
.hero-photo{flex:1;background:linear-gradient(180deg,#c9d4dc 0%,#8aa1a8 40%,#5d6e62 70%,#a6503a 100%)}

.intro{height:110px;flex:none;padding:22px 56px 0;columns:2;column-gap:36px}

.main{height:780px;flex:none;display:flex;gap:30px;padding:10px 56px 30px}
.values{width:350px;background:var(--brown);padding:30px 28px;color:#fff;display:flex;flex-direction:column;justify-content:space-between}
.values h2{font-size:26px;font-weight:700;display:flex;align-items:center;gap:10px}
.values h2 span{color:var(--gold)}
.values h2 i{width:28px;height:28px;border:3px solid var(--gold);border-radius:50%;display:inline-block}
.value{display:flex;gap:18px;align-items:flex-start}
.value-icon{width:60px;height:60px;background:var(--gold);flex:none;display:flex;align-items:center;justify-content:center}
.value h3{font-size:20px;font-weight:700;color:var(--gold);margin-bottom:6px}
.value p{color:#e8d9cc;font-size:13px;line-height:1.5}

.side{flex:1;display:flex;flex-direction:column;gap:18px}
.event{display:flex;gap:18px;align-items:flex-start}
.date{width:84px;flex:none;background:var(--brown);color:#fff;text-align:center;font-family:"Montserrat",sans-serif;font-weight:800;padding:6px 0}
.date b{display:block;font-size:26px;line-height:1.1;color:var(--gold)}
.date small{font-size:13px}
.event p{font-size:13px}
.feature{background:var(--brown);flex:1;display:flex;flex-direction:column}
.feature-head{background:var(--gold);color:var(--brown-dark);font-family:"Montserrat",sans-serif;font-weight:800;font-size:18px;padding:12px 20px;text-align:center}
.feature-body{display:flex;gap:24px;padding:30px 28px;flex:1;align-items:center}
.fun-badge{width:120px;height:120px;border-radius:50%;background:var(--gold);flex:none;display:flex;align-items:center;justify-content:center;text-align:center;font-family:"Montserrat",sans-serif;font-weight:800;font-size:26px;line-height:1;color:var(--brown-dark)}
.fun-list{list-style:none;display:flex;flex-direction:column;gap:22px}
.fun-list li{color:#f0e2d6;font-size:14px;line-height:1.5;padding-left:20px;position:relative}
.fun-list li::before{content:"";position:absolute;left:0;top:7px;width:8px;height:8px;background:var(--gold)}

.footer{height:66px;flex:none;background:var(--brown);display:flex;align-items:center;justify-content:space-between;padding:0 56px;color:#fff;font-family:"Montserrat",sans-serif;font-weight:600;font-size:15px}
.follow{display:flex;align-items:center;gap:10px}
.follow i{width:22px;height:22px;border-radius:50%;background:var(--gold);display:inline-block}

/* page 2 */
.top{height:620px;flex:none;display:flex;gap:0}
.eom-feature{width:520px;display:flex;flex-direction:column}
.eom-photo{height:400px;background:linear-gradient(160deg,#8c5a3a,#3e2416);padding:40px 36px}
.eom-photo h2{font-size:46px;font-weight:800;line-height:1.02;color:#fff}
.eom-photo h2 span{display:block;font-size:30px;color:var(--gold)}
.eom-photo p{color:#ecdccd;margin-top:18px;width:300px}
.business{padding:24px 36px 0}
.business h2{font-size:22px;font-weight:800;color:var(--gold);margin-bottom:10px}
.business p{margin-bottom:8px}
.eom-side{flex:1;padding:20px 36px 0 0;display:flex;flex-direction:column;gap:14px}
.bar-head{background:var(--brown);color:#fff;font-family:"Montserrat",sans-serif;font-weight:700;font-size:18px;padding:10px 16px}
.bar-head span{color:var(--gold)}
.profile{display:flex;gap:18px;height:140px}
.profile .photo{width:170px;height:140px;flex:none;background:linear-gradient(135deg,#c7c7c7,#6d6d6d)}
.lists{display:flex;gap:16px;height:190px}
.list{flex:1}
.list h3{font-size:14px;font-weight:800;color:var(--brown);margin-bottom:10px;line-height:1.2}
.list h3 span{color:var(--gold)}
.list ol{list-style:none;display:flex;flex-direction:column;gap:8px}
.list li{font-size:12.5px;display:flex;gap:8px;align-items:center}
.list li b{background:var(--gold);color:var(--brown-dark);width:20px;height:18px;font-size:11px;display:flex;align-items:center;justify-content:center}
.chair{width:120px;flex:none;background:linear-gradient(160deg,#f1f1f1,#bdbdbd)}
.hiring{height:180px;display:flex;background:var(--brown)}
.hiring-text{padding:28px 24px;width:230px}
.hiring-text h2{font-size:32px;font-weight:800;line-height:1;color:#fff}
.hiring-text h2 span{color:var(--gold);display:block}
.hiring-text p{color:#e8d9cc;font-size:12px;margin-top:10px}
.hiring .photo{flex:1;background:linear-gradient(135deg,#d8c7a6,#8f7a57)}

.columns{height:300px;flex:none;display:grid;grid-template-columns:repeat(3,1fr);gap:30px;padding:28px 36px 20px}
.columns h3{font-size:17px;font-weight:800;color:var(--brown);border-bottom:3px solid var(--gold);padding-bottom:8px;margin-bottom:10px}
.columns h4{font-size:13px;font-weight:700;color:var(--gold);margin:10px 0 4px}
.columns p{font-size:12.5px}

.band{height:360px;flex:none;display:flex;gap:24px;padding:0 36px 30px}
.band .photo{flex:1;background:linear-gradient(160deg,#8a8f94,#5b4a3a)}
.calendar{width:340px;background:var(--gold);padding:22px}
.calendar h3{font-size:22px;font-weight:800;color:var(--brown-dark);margin-bottom:4px}
.calendar .month{font-family:"Montserrat",sans-serif;font-weight:700;font-size:13px;color:var(--brown);margin-bottom:10px}
.calendar table{width:100%;border-collapse:collapse;background:#fff}
.calendar th{background:var(--brown);color:#fff;font-size:11px;font-family:"Montserrat",sans-serif;padding:5px 0}
.calendar td{text-align:center;font-size:11px;padding:7px 0;border:1px solid var(--rule)}
.calendar td.mark{background:var(--gold-soft);font-weight:700}
</style>
</head>
<body>

<section class="page page-one">
  <header class="masthead">
    <div class="brand"><span class="brand-square"></span><span class="brand-name">HALVARD QUARRY</span></div>
    <div class="title-block">
      <div class="kicker">HALVARD MATTERS</div>
      <h1 class="title"><span class="news">NEWS</span><span class="letter">LETTER</span></h1>
    </div>
  </header>

  <section class="hero">
    <div class="hero-panel">
      <h2>OUR PEOPLE. OUR PASSION.</h2>
      <p>Each month we share the stories, milestones and faces that keep our site moving forward. Thank you for the care and effort you bring to every shift, above and below ground.</p>
    </div>
    <div class="hero-photo" role="img" aria-label="Landscape photo of a river valley near the mine site"></div>
  </section>

  <section class="intro">
    <p>Production held steady this month and our teams reached several new safety milestones. Read on for updates from every department, recent hires and a few dates to mark on your calendar.</p>
    <p>We also welcome feedback on this newsletter. Share your ideas, photos and stories with your supervisor so we can feature them in an upcoming issue.</p>
  </section>

  <section class="main">
    <aside class="values">
      <h2><i></i>OUR <span>VALUES</span></h2>
      <div class="value"><div class="value-icon"><svg width="28" height="28" viewBox="0 0 26 26"><path d="M13 3 L22 7 V13 C22 18 18 22 13 23 C8 22 4 18 4 13 V7 Z" fill="none" stroke="#4e2917" stroke-width="2.5"/></svg></div><div><h3>Be Safe</h3><p>Look out for yourself and your crew on every task, every shift.</p></div></div>
      <div class="value"><div class="value-icon"><svg width="28" height="28" viewBox="0 0 26 26"><path d="M5 14 L11 20 L21 6" fill="none" stroke="#4e2917" stroke-width="3"/></svg></div><div><h3>Be Honest</h3><p>Speak openly and do what you say you will do.</p></div></div>
      <div class="value"><div class="value-icon"><svg width="28" height="28" viewBox="0 0 26 26"><circle cx="13" cy="13" r="9" fill="none" stroke="#4e2917" stroke-width="2.5"/><path d="M13 8 V13 L17 16" fill="none" stroke="#4e2917" stroke-width="2.5"/></svg></div><div><h3>Be Responsible</h3><p>Own your work and care for the land we share.</p></div></div>
      <div class="value"><div class="value-icon"><svg width="28" height="28" viewBox="0 0 26 26"><circle cx="9" cy="10" r="3.5" fill="#4e2917"/><circle cx="17" cy="10" r="3.5" fill="#4e2917"/><path d="M3 21 C4 15 14 15 15 21 M11 21 C12 15 22 15 23 21" fill="none" stroke="#4e2917" stroke-width="2.2"/></svg></div><div><h3>Be Respectful</h3><p>Treat every colleague and neighbour with dignity.</p></div></div>
      <div class="value"><div class="value-icon"><svg width="28" height="28" viewBox="0 0 26 26"><path d="M13 3 L16 10 L23 10.5 L17.5 15 L19.5 22 L13 18 L6.5 22 L8.5 15 L3 10.5 L10 10 Z" fill="#4e2917"/></svg></div><div><h3>Be Great</h3><p>Aim higher and help others reach their best.</p></div></div>
    </aside>

    <div class="side">
      <div class="event"><div class="date"><b>JAN</b><small>2024</small></div><p>Annual safety review completed with every crew taking part. Results will be posted on the board.</p></div>
      <div class="event"><div class="date"><b>FEB</b><small>2024</small></div><p>New equipment arrives at the mill site, with training sessions scheduled for all operators.</p></div>
      <div class="event"><div class="date"><b>FEB</b><small>2024</small></div><p>Community open house planned in town. Volunteers are welcome to sign up at the front office.</p></div>
      <div class="feature">
        <div class="feature-head">LOREM IPSUM COLOR DOLOR</div>
        <div class="feature-body">
          <div class="fun-badge">FUN<br>FACT</div>
          <ul class="fun-list">
            <li>Copper has been used by people for more than ten thousand years.</li>
            <li>A single electric car holds around eighty kilograms of copper.</li>
            <li>Copper can be recycled again and again without losing quality.</li>
            <li>Our site sees nearly twenty hours of daylight in June.</li>
            <li>Our first shipment of concentrate left the site by truck in winter.</li>
          </ul>
        </div>
      </div>
    </div>
  </section>

  <footer class="footer"><span>brelcoreworks.com</span><span class="follow">Follow Us <i></i><i></i><i></i></span></footer>
</section>

<section class="page page-two">
  <section class="top">
    <div class="eom-feature">
      <div class="eom-photo" role="img" aria-label="Photo of a miner in safety gear at the site">
        <h2>EMPLOYEE<span>OF THE MONTH</span></h2>
        <p>Recognising a team member who lives our values every day on the job.</p>
      </div>
      <div class="business">
        <h2>BUSINESS GOOD FOR LIFE</h2>
        <p>Our work supplies metal for clean power, homes and tools used around the world. Every tonne we ship starts with the skill of our people.</p>
        <p>This month we look at how careful planning keeps our costs down and our crews safe through the coldest weeks of the year.</p>
      </div>
    </div>
    <div class="eom-side">
      <div class="bar-head">EMPLOYEE <span>OF THE MONTH</span></div>
      <div class="profile">
        <div class="photo" role="img" aria-label="Portrait photo of the employee of the month"></div>
        <p>Our honouree led the crew through a record month with zero incidents and went out of the way to mentor two new hires. Thank you for setting the standard for the whole site.</p>
      </div>
      <div class="lists">
        <div class="list"><h3>MONTHLY<br><span>TENURE</span></h3><ol><li><b>10</b>Name Surname</li><li><b>8</b>Name Surname</li><li><b>5</b>Name Surname</li><li><b>5</b>Name Surname</li><li><b>3</b>Name Surname</li></ol></div>
        <div class="list"><h3>MONTHLY<br><span>NEW HIRES</span></h3><ol><li><b>1</b>Name Surname</li><li><b>2</b>Name Surname</li><li><b>3</b>Name Surname</li><li><b>4</b>Name Surname</li><li><b>5</b>Name Surname</li></ol></div>
        <div class="chair" role="img" aria-label="Photo of an empty office chair"></div>
      </div>
      <div class="hiring">
        <div class="hiring-text"><h2>WE ARE<span>HIRING</span></h2><p>Know someone great? Refer them today and help our team grow.</p></div>
        <div class="photo" role="img" aria-label="Photo of a hand holding a megaphone"></div>
      </div>
    </div>
  </section>

  <section class="columns">
    <div><h3>Community Engagement</h3><h4>Local School Visit</h4><p>Our geology team shared rock samples with students in grade six.</p><h4>Food Drive</h4><p>Staff collected over two hundred items for the local pantry.</p><h4>Trail Cleanup</h4><p>Volunteers cleared the river path ahead of the spring thaw.</p></div>
    <div><h3>Upcoming Holidays/Events</h3><h4>Family Day</h4><p>Site offices closed. Operations crews follow the posted schedule.</p><h4>Winter Games</h4><p>Join the camp teams for snowshoe races and a bonfire night.</p><h4>Safety Week</h4><p>Daily talks and refresher drills for every department.</p></div>
    <div><h3>Social Club</h3><h4>Movie Night</h4><p>Fridays in the rec hall, with snacks provided by the kitchen.</p><h4>Fitness Challenge</h4><p>Log your steps and compete for prizes across all crews.</p><h4>Curling League</h4><p>New players welcome. Sign up sheets are at the camp desk.</p></div>
  </section>

  <section class="band">
    <div class="photo" role="img" aria-label="Group photo of crew members in hard hats"></div>
    <div class="calendar">
      <h3>IMPORTANT DATES</h3>
      <div class="month">FEBRUARY 2024</div>
      <table>
        <tr><th>S</th><th>M</th><th>T</th><th>W</th><th>T</th><th>F</th><th>S</th></tr>
        <tr><td></td><td></td><td></td><td></td><td>1</td><td>2</td><td>3</td></tr>
        <tr><td>4</td><td>5</td><td>6</td><td>7</td><td>8</td><td class="mark">9</td><td>10</td></tr>
        <tr><td>11</td><td>12</td><td>13</td><td>14</td><td>15</td><td>16</td><td>17</td></tr>
        <tr><td>18</td><td class="mark">19</td><td>20</td><td>21</td><td>22</td><td>23</td><td>24</td></tr>
        <tr><td>25</td><td>26</td><td>27</td><td class="mark">28</td><td>29</td><td></td><td></td></tr>
      </table>
    </div>
  </section>

  <footer class="footer"><span>www.brelcoreworks.com</span><span class="follow">Follow Us <i></i><i></i><i></i></span></footer>
</section>

</body>
</html>
```